Professional Hairdresser needs powerful, clever, simple, modern business card

I need a professional, clever, powerful, bold, attractive, modern/simplistic business card.
I specialize in dimensional hair color, precision haircutting, modern classic design, and signature finishes.
I believe in advanced education, continued training with emphasis on perfect practice, and strive to be the best at what I do.
I am trained by the industry's best and have passion for what I do, I want my business card to reflect my talents, education, capabilities, signature color techniques and design and confidence.
I want to be known as reputable, bold, artistic, aware, classic yet modern, innovative, creative, dimensional, knowledgeable, and educated.
I want something bold, simple, elegant, modern, clever, and legible.
My personal style is progressive, modern, eclectic, clean with modern luxury comfort style.
I love the use of black and white, to creative visual interest and texture. I think putting black as a solid background with white bold font makes the words jump/glow to the eye. I also think a stark white background with bold black fonts looks great, maybe with a punch of red. It is simple, clean, elegant.
I have a QR code I would like to include on the card but have no idea how to make it visually pleasing or make sense.
I do not have a set logo and am not sure if this needs to be done first or if the business card should be done first.

Target Market(s)

Early 20's-mid 60's, female and male, fashion aware, people who can afford my prices, appreciate value

Industry/Entity Type

Training

Requirements
Must have
• I would like to incorporate the QR code I have if possible.
I would like to have my name and contact info.
I would like my logo (or maybe have my logo be RT in a font like listed below).
I would like the fonts to be modern, bold, clean, readable.
Fonts I have looked at are: The font used on the book called: Vexaro A Hundred Years of Hue" I really love. I have looked at glyphvault.example for font and found "Georgiquas", but the designer wanted 200 euros which I just dont have at the time. Others I looked at include "Lin Libertine", Alien-Encounters-solid-regular-italic".
I love font used in the picture I included with the Tobin.Ashcroft ad.
Clean, modern, professional, legible, structured.
Nice to have
• I envision a black background with bold, modern, simple, font in white creating the effect of the words jumping off the card, visually apparent and glowing. Like a really expensive restaurant with a sign that you cant miss because the name is in bright white on black background, simple, bold, modern but not futuristic, powerful, clever, elegant, and draws the eye making it unforgetable. Perhaps layering black and white in order to where the font will be in white.
I see balance and chic.
Perhaps
Should not have
• I appreciate the trends in business design, but realize trends come and go and not sure if having something "trendy" is advisable for me. Having said that, I like creative modern design and sometimes current trends are important in design. I do like red as accent color, the primary blue color, blue on the PixelForum page, the masculine/florescent purple, and the neo bold yellow and the primary color shade of yellow.
I do not want clutter.
I do not want any fonts that are swirly, old-world calligraphy, script, or penmanship style.
I do not want picture of scissors, heads of old-school beauty school hair, or barber poles.

```html
<!DOCTYPE html>
<html lang="en">
<head>
<meta charset="utf-8">
<title>Rafe Tate — Business Card</title>
<link rel="stylesheet" href="https://fonts.googleapis.com/css2?family=Tinos&display=swap">
<style>
  :root {
    --ink: #000000;
    --paper: #f7f7f7;
    --white: #ffffff;
    --rule: #6f6f6f;
  }
  * { margin: 0; padding: 0; box-sizing: border-box; }
  html, body { width: 1200px; height: 693px; overflow: hidden; background: var(--paper); }
  .card {
    position: relative;
    width: 1200px;
    height: 693px;
    background: var(--paper);
    overflow: hidden;
  }
  .card__front {
    position: absolute;
    left: 0; top: 0;
    width: 1200px; height: 550px;
    background: var(--ink);
  }
  .wordmark {
    position: absolute;
    left: 0; right: 0;
    top: 120px;
    text-align: center;
    font-family: "Tinos", serif;
    font-weight: 400;
    font-size: 300px;
    line-height: 1;
    color: var(--white);
    white-space: nowrap;
  }
  .card__rule {
    position: absolute;
    left: 8px; right: 0;
    top: 493px;
    height: 18px;
    background: var(--rule);
  }
  .website {
    position: absolute;
    left: 0; right: 0;
    top: 562px;
    text-align: center;
    font-family: "Tinos", serif;
    font-size: 44px;
    line-height: 1;
    color: var(--ink);
    white-space: nowrap;
  }
  .socials {
    position: absolute;
    left: 0; right: 0;
    top: 620px;
    height: 60px;
    display: flex;
    justify-content: center;
    align-items: center;
    gap: 56px;
    font-family: "Tinos", serif;
    font-size: 36px;
    color: var(--ink);
    list-style: none;
  }
  .socials__item {
    display: flex;
    align-items: center;
    gap: 10px;
  }
  .socials__mark {
    width: 22px; height: 22px;
    background: var(--ink);
  }
</style>
</head>
<body>
  <main class="card">
    <section class="card__front">
      <h1 class="wordmark">TATE</h1>
      <div class="card__rule"></div>
    </section>
    <p class="website">WWW.RAFETATE.PRO.EXAMPLE</p>
    <ul class="socials">
      <li class="socials__item"><span class="socials__mark"></span>Flitter</li>
      <li class="socials__item"><span class="socials__mark"></span>Friendline</li>
      <li class="socials__item"><span class="socials__mark"></span>Netlink</li>
      <li class="socials__item"><span class="socials__mark"></span>Reelbox</li>
    </ul>
  </main>
</body>
</html>
```